menu board design: harbor burger

we are a burger restaurant.
we need to re design our menu board to fit within the new design of the restaurant. we are after something simple and easy to read. the overall look and feel of the design should be inline with the design of the shop.

Target Market(s)

18-40 male and female

Colors

Designer to choose colors to be used in the design.

Requirements
Must have
• easy to read. good layout. white background. branding included in design.

```html
<!DOCTYPE html>
<html lang="en">
<head>
<meta charset="utf-8">
<title>Harbor Burger — Menu Board</title>
<link rel="stylesheet" href="https://fonts.googleapis.com/css2?family=Bangers&family=Signika:wght@300;400;600;700&display=swap">
<style>
  :root {
    --paper: #f7f7f5;
    --band-blue: #0f5f93;
    --ink-blue: #1b4a9a;
    --brush-yellow: #e2b81f;
    --item-yellow: #e2b11c;
    --heading-red: #bf1f2e;
    --body-ink: #333333;
    --rule-blue: #2a56a8;
    --illus-tone: #dfe6f1;
  }
  * { box-sizing: border-box; margin: 0; padding: 0; }
  html, body { width: 1200px; height: 600px; overflow: hidden; background: var(--paper); }
  body { font-family: "Signika", sans-serif; color: var(--body-ink); }

  .menu-board { position: relative; width: 1200px; height: 600px; background: var(--paper); overflow: hidden; }
  .edge-band { position: absolute; top: 0; bottom: 0; width: 36px; background: var(--band-blue); }
  .edge-band--left { left: 0; }
  .edge-band--right { right: 0; }

  .abs { position: absolute; }

  .section-title {
    position: absolute; display: flex; align-items: center; justify-content: center;
    background: var(--brush-yellow); font-family: "Bangers", sans-serif;
    letter-spacing: 1px; line-height: 1; font-weight: 400;
  }
  .section-title--blue { color: var(--ink-blue); font-size: 31px; }
  .section-title--red { color: var(--heading-red); font-size: 22px; }

  .intro { font-size: 11px; line-height: 14.4px; text-align: center; font-weight: 300; color: var(--body-ink); }
  .sub-label { font-size: 11.5px; font-weight: 600; color: var(--ink-blue); text-align: center; letter-spacing: .3px; }

  .item { position: absolute; width: 314px; }
  .item__head { display: flex; align-items: baseline; color: var(--item-yellow); font-weight: 600; font-size: 11.5px; letter-spacing: .3px; }
  .item__leader { flex: 1; border-bottom: 1.5px dotted var(--item-yellow); margin: 0 2px 3px; }
  .item__desc { font-size: 10.6px; line-height: 13.2px; font-weight: 300; color: var(--body-ink); text-align: justify; margin-top: 2px; }

  .brand { text-align: center; }
  .brand__name { font-family: "Signika", sans-serif; font-weight: 700; color: var(--ink-blue); font-size: 86px; line-height: 94px; }
  .brand__tagline { display: inline-block; margin-top: 18px; font-size: 13.5px; letter-spacing: 5.4px; color: var(--ink-blue); font-weight: 400; padding-bottom: 4px; border-bottom: 2px solid var(--ink-blue); }

  .star-doodle { position: absolute; width: 26px; height: 26px; border-radius: 50%; background: var(--illus-tone); }

  .divider { position: absolute; top: 350px; border-top: 2px dashed var(--rule-blue); }

  .step-pill { position: absolute; background: var(--brush-yellow); color: var(--ink-blue); font-weight: 600; font-size: 11px; display: flex; align-items: center; justify-content: center; height: 17px; }

  .option { position: absolute; color: var(--item-yellow); font-weight: 600; font-size: 11.5px; line-height: 14.4px; }
  .option__row { display: flex; align-items: baseline; }
  .option__leader { flex: 1; border-bottom: 1px dotted var(--item-yellow); margin: 0 2px 3px; }
  .option__price { font-weight: 400; }
  .topping { position: absolute; width: 162px; color: var(--item-yellow); font-size: 10.8px; line-height: 14.4px; font-weight: 300; text-align: justify; }
  .topping b { font-weight: 600; }

  .side-row { display: flex; align-items: baseline; color: var(--item-yellow); font-weight: 600; font-size: 15px; line-height: 18px; letter-spacing: .4px; }
  .side-row .item__leader { margin-bottom: 4px; }

  .illustration { position: absolute; background: var(--illus-tone); border-radius: 6px; }

  .pack { position: absolute; width: 158px; }
  .pack .option__row { color: var(--item-yellow); font-weight: 600; font-size: 11.5px; }
  .sauce-choice { color: var(--ink-blue); font-weight: 600; font-size: 11.5px; line-height: 14.5px; letter-spacing: .3px; }
</style>
</head>
<body>
<main class="menu-board">
  <div class="edge-band edge-band--left"></div>
  <div class="edge-band edge-band--right"></div>

  <div class="star-doodle" style="left:66px;top:20px" role="img" aria-label="Hand-drawn star doodle"></div>
  <div class="star-doodle" style="left:66px;top:556px" role="img" aria-label="Hand-drawn star doodle"></div>
  <div class="star-doodle" style="left:1115px;top:20px" role="img" aria-label="Hand-drawn star doodle"></div>
  <div class="star-doodle" style="left:1115px;top:538px" role="img" aria-label="Hand-drawn star doodle"></div>

  <section class="beef-burgers">
    <h2 class="section-title section-title--blue" style="left:120px;top:34px;width:208px;height:32px">BEEF BURGERS</h2>
    <p class="intro abs" style="left:66px;top:69px;width:322px">All our patties are 100% natural beef. We know because we<br>grind it ourselves, smashed to order on a hot grill rite in from<br>of you</p>
    <p class="sub-label abs" style="left:66px;top:123px;width:322px">DOUBLE PATTY ADD 4</p>
    <div class="item" style="left:67px;top:141px"><div class="item__head"><span>CLASSIC BEEF</span><span class="item__leader"></span><span>8.9</span></div><p class="item__desc">Shredded lettuce, sliced tomato, caramelised onions, beetroot and BBQ sauce on a buttered sesame seed bum.</p></div>
    <div class="item" style="left:67px;top:193px"><div class="item__head"><span>CHEESE BURGER</span><span class="item__leader"></span><span>9.5</span></div><p class="item__desc">Dill pickles, minced onion, american cheese, mustard and ketchup on soft milk bun.</p></div>
    <div class="item" style="left:67px;top:240px"><div class="item__head"><span>FLAME GRILL</span><span class="item__leader"></span><span>9.5</span></div><p class="item__desc">Shredded lettuce, sliced tomato, minced onion, dill pickles, american cheese, mayo and ketchup on a soft bun.</p></div>
    <div class="item" style="left:67px;top:289px"><div class="item__head"><span>BIG STACK</span><span class="item__leader"></span><span>9.9</span></div><p class="item__desc">Shredded lettuce, dil pickles, minced onion, american cheese and special sauce on a soft milk bun.</p></div>
  </section>

  <header class="brand abs" style="left:430px;top:62px;width:340px">
    <h1 class="brand__name">Harbor<br>Burger</h1>
    <p class="brand__tagline">CLASSICS FOR A REASON</p>
  </header>

  <section class="chicken-burgers">
    <h2 class="section-title section-title--blue" style="left:818px;top:34px;width:264px;height:32px">CHICKEN BURGERS</h2>
    <p class="intro abs" style="left:806px;top:69px;width:322px">All our patties are 100% natural beef. We know because we<br>grind it ourselves, smashed to order on a hot grill rite in from<br>of you</p>
    <p class="sub-label abs" style="left:806px;top:122px;width:322px">DOUBLE PATTY ADD 4</p>
    <div class="item" style="left:811px;top:140px"><div class="item__head"><span>CLASSIC BEEF</span><span class="item__leader"></span><span>8.9</span></div><p class="item__desc">Shredded lettuce, sliced tomato, caramelised onions, beetroot and BBQ sauce on a buttered sesame seed bum.</p></div>
    <div class="item" style="left:811px;top:192px"><div class="item__head"><span>CHEESE BURGER</span><span class="item__leader"></span><span>9.5</span></div><p class="item__desc">Dill pickles, minced onion, american cheese, mustard and ketchup on soft milk bun.</p></div>
    <div class="item" style="left:811px;top:239px"><div class="item__head"><span>FLAME GRILL</span><span class="item__leader"></span><span>9.5</span></div><p class="item__desc">Shredded lettuce, sliced tomato, minced onion, dill pickles, american cheese, mayo and ketchup on a soft bun.</p></div>
    <div class="item" style="left:811px;top:287px"><div class="item__head"><span>TRUFFLED</span><span class="item__leader"></span><span>9.9</span></div><p class="item__desc">Rocket, caramelised onion, dill pickles, havarti cheese and truffle infused mayo on a soft milk bun.</p></div>
  </section>

  <div class="divider" style="left:92px;width:376px"></div>
  <div class="divider" style="left:718px;width:364px"></div>

  <section class="loaded-fries">
    <h2 class="section-title section-title--red" style="left:116px;top:366px;width:230px;height:30px">NACHOS &amp; LOADED FRIES</h2>
    <div class="step-pill" style="left:116px;top:423px;width:74px">STEP ONE</div>
    <div class="step-pill" style="left:292px;top:423px;width:74px">STEP TWO</div>
    <p class="sub-label abs" style="left:95px;top:452px;width:120px">CHOOSE EITHER,</p>
    <p class="sub-label abs" style="left:273px;top:452px;width:120px">CHOOSE ONE,</p>
    <div class="option" style="left:65px;top:481px;width:180px"><div class="option__row"><span>SEASONED FRIES</span><span class="option__leader"></span><span class="option__price">9.9</span></div></div>
    <div class="option" style="left:65px;top:510px;width:180px"><div>OR FRESHLY COOKED</div><div class="option__row"><span>CORN CHIPS</span><span class="option__leader"></span><span class="option__price">11.5</span></div></div>
    <p class="topping" style="left:252px;top:481px"><b>GUACAMOLE</b> salsa fresca, guacamole, jalapeñoz, cheese sauce and sour cream.<br><b>BEEF CHILLI</b> salsa fresca, beef chilli, jalapeños, cheese sauce and sour cream.</p>
  </section>

  <section class="sides">
    <h2 class="section-title section-title--blue" style="left:527px;top:339px;width:135px;height:36px;font-size:34px">SIDES</h2>
    <div class="abs" style="left:483px;top:395px;width:220px">
      <div class="side-row"><span>FRIES</span><span class="item__leader"></span><span>3.5</span></div>
      <div class="side-row"><span>KENTUCKY TENDERS</span><span class="item__leader"></span><span>6.9</span></div>
    </div>
    <p class="item__desc abs" style="left:483px;top:444px;width:221px;font-size:10.5px;line-height:13.2px">Breaded and fried chicken tenders with secret seasoning. <b style="font-weight:600">(2 PCS).</b></p>
    <div class="illustration" style="left:495px;top:498px;width:109px;height:64px" role="img" aria-label="Sketch illustration of a burger"></div>
    <div class="illustration" style="left:627px;top:474px;width:55px;height:88px" role="img" aria-label="Sketch illustration of an iced drink"></div>
  </section>

  <section class="buffalo-ribs">
    <h2 class="section-title section-title--red" style="left:832px;top:366px;width:228px;height:30px">BUFFALO CHICKEN RIBS</h2>
    <p class="intro abs" style="left:788px;top:415px;width:330px">Buffalo style fried chicken ribs smothered in one dur mouth-watering<br>sauce. Served with a side of ranch sauce.</p>
    <div class="pack" style="left:792px;top:469px"><div class="option__row"><span>6 PACK</span><span class="option__leader"></span><span class="option__price">6.9</span></div></div>
    <div class="pack" style="left:792px;top:498px"><div class="option__row"><span>12 PACK</span><span class="option__leader"></span><span class="option__price">12.9</span></div></div>
    <div class="pack" style="left:792px;top:527px"><div class="option__row"><span>24 PACK</span><span class="option__leader"></span><span class="option__price">23.9</span></div></div>
    <p class="sauce-choice abs" style="left:986px;top:485px">CLASSIC HOT SAUCE<br>OR SMOKY BBQ</p>
  </section>
</main>
</body>
</html>
```